Business Card Design for TrailReady

TrailReady is an online e-commerce store specializing in Outdoors Gear such as camping equipment, hunting and shooting equipment, tactical gear and more. See complete line at trailready-gear.example
Logo: http://www.trailready-gear.example/media/ID/Ready.jpg
http://www.trailready-gear.example/media/ID/TrailReady-blue.jpg

Target Market(s)

20-40 Male

Industry/Entity Type

E-Commerce

```html
<!DOCTYPE html>
<html lang="en">
<head>
<meta charset="utf-8">
<title>TrailReady Business Card Variations</title>
<link rel="stylesheet" href="https://fonts.googleapis.com/css2?family=Alegreya+Sans:wght@400;700&family=Roboto:wght@400&display=swap">
<style>
  :root {
    --navy: #0b3a66;
    --white: #ffffff;
    --kraft: #d8b887;
    --kraft-light: #e2c699;
    --ink-brown: #3a2a1c;
    --yellow: #f7c600;
    --yellow-light: #ffdc45;
    --heading: #222222;
    --shadow: rgba(0, 0, 0, 0.25);
  }
  * { box-sizing: border-box; margin: 0; padding: 0; }
  html, body { width: 981px; height: 1200px; overflow: hidden; background: var(--white); }
  body { position: relative; font-family: "Alegreya Sans", "Segoe UI", sans-serif; }

  .sheet-title, .column-head {
    position: absolute; font-family: "Roboto", Arial, sans-serif; font-weight: 400;
    color: var(--heading); text-align: center;
  }
  .sheet-title { top: 44px; left: 0; width: 981px; font-size: 36px; }
  .column-head { top: 106px; width: 408px; font-size: 34px; }
  .column-head.front { left: 69px; }
  .column-head.back { left: 499px; }

  .card {
    position: absolute; width: 408px; height: 225px; overflow: hidden;
    box-shadow: 0 1px 5px var(--shadow);
  }
  .card.front { left: 69px; }
  .card.back { left: 499px; }
  .row-1 { top: 165px; } .row-2 { top: 413px; } .row-3 { top: 663px; } .row-4 { top: 911px; }

  .navy { background: var(--navy); color: var(--white); }
  .paper { background: var(--white); color: var(--navy); }
  .kraft { background: linear-gradient(160deg, var(--kraft-light), var(--kraft)); }

  .brand { position: absolute; display: flex; align-items: center; gap: 10px; }
  .brand-dot { width: 40px; height: 40px; border-radius: 50%; border: 2.5px solid currentColor; flex: none; }
  .brand-text { display: flex; flex-direction: column; }
  .brand-name { font-weight: 700; font-size: 30px; line-height: 1; }
  .tagline { font-size: 13px; letter-spacing: 1.1px; margin-top: 4px; white-space: nowrap; }

  .front-centered .brand { left: 38px; top: 84px; }

  .contact { position: absolute; font-size: 11px; line-height: 15px; white-space: nowrap; }
  .person-name { position: absolute; font-size: 19px; line-height: 1.1; white-space: nowrap; }
  .person-title { position: absolute; font-size: 14px; white-space: nowrap; }

  .wordmark { position: absolute; font-weight: 700; text-align: center; line-height: 1; white-space: nowrap; }

  .side-panel { position: absolute; left: 0; top: 0; width: 204px; height: 225px; background: var(--navy); }

  .band { position: absolute; left: 0; top: 0; width: 408px; height: 225px; }
  .tier-3 .brand, .tier-4 .brand { left: 38px; top: 24px; color: var(--white); }

  .frame { position: absolute; border: 2px solid var(--ink-brown); display: flex; align-items: center; justify-content: center; }
  .frame .symbol { width: 70%; height: 70%; background: rgba(58, 42, 28, 0.35); }
</style>
</head>
<body>
  <h1 class="sheet-title">Variations</h1>
  <h2 class="column-head front">1 side</h2>
  <h2 class="column-head back">2 side</h2>

  <section class="card front row-1 navy front-centered">
    <div class="brand">
      <span class="brand-dot"></span>
      <div class="brand-text">
        <span class="brand-name">TrailReady.com</span>
        <span class="tagline">Ready for Every Trail and Adventure</span>
      </div>
    </div>
  </section>
  <section class="card back row-1 paper">
    <div class="contact" style="left:36px;top:22px;">www.trailready-gear.example<br>PO BOX 327<br>Pinecrest, IL 60999<br>orders@trailready-gear.example</div>
    <div class="wordmark" style="left:250px;top:66px;width:140px;font-size:28px;">TrailReady</div>
    <div class="person-name" style="left:36px;top:160px;">Marek Dolan</div>
    <div class="person-title" style="left:36px;top:184px;">Purchasing Manager</div>
    <div class="contact" style="left:280px;top:166px;">Cell: 555 014 2200<br>Office: 555 018 7341</div>
  </section>

  <section class="card front row-2 navy front-centered">
    <div class="brand">
      <span class="brand-dot"></span>
      <div class="brand-text">
        <span class="brand-name">TrailReady.com</span>
        <span class="tagline">Ready for Every Trail and Adventure</span>
      </div>
    </div>
  </section>
  <section class="card back row-2 paper">
    <div class="side-panel"></div>
    <div class="wordmark" style="left:0;top:97px;width:204px;font-size:30px;color:var(--white);">TrailReady</div>
    <div class="person-name" style="left:244px;top:30px;">Marek Dolan</div>
    <div class="person-title" style="left:244px;top:53px;">Purchasing Manager</div>
    <div class="contact" style="left:244px;top:92px;">Cell: 555 014 2200<br>Office: 555 018 7341</div>
    <div class="contact" style="left:244px;top:140px;">www.trailready-gear.example<br>PO BOX 327<br>Pinecrest, IL 60999<br>orders@trailready-gear.example</div>
  </section>

  <section class="card front row-3 kraft tier-3">
    <svg class="band" viewBox="0 0 408 225" aria-hidden="true">
      <polygon points="0,0 408,0 408,160 160,160 140,142 0,142" fill="var(--navy)"/>
    </svg>
    <div class="brand">
      <span class="brand-dot"></span>
      <div class="brand-text">
        <span class="brand-name">TrailReady.com</span>
        <span class="tagline">Ready for Every Trail and Adventure</span>
      </div>
    </div>
    <div class="contact" style="left:245px;top:82px;color:var(--white);">www.trailready-gear.example<br>PO BOX 327<br>Pinecrest, IL 60999<br>orders@trailready-gear.example</div>
    <div class="person-name" style="left:34px;top:165px;color:var(--ink-brown);font-size:18px;">Marek Dolan</div>
    <div class="person-title" style="left:34px;top:186px;color:var(--ink-brown);font-size:13px;">Purchasing Manager</div>
    <div class="contact" style="left:245px;top:172px;color:var(--ink-brown);">Cell: 555 014 2200<br>Office: 555 018 7341</div>
  </section>
  <section class="card back row-3 kraft">
    <div class="frame" style="left:54px;top:67px;width:86px;height:90px;"><div class="symbol" role="img" aria-label="Handling symbol: this side up arrows"></div></div>
    <div class="frame" style="left:161px;top:67px;width:86px;height:90px;"><div class="symbol" role="img" aria-label="Handling symbol: keep dry umbrella"></div></div>
    <div class="frame" style="left:263px;top:67px;width:88px;height:90px;"><div class="symbol" role="img" aria-label="Handling symbol: fragile glass"></div></div>
  </section>

  <section class="card front row-4 tier-4" style="background:linear-gradient(180deg,var(--yellow) 80%,var(--yellow-light));">
    <svg class="band" viewBox="0 0 408 225" aria-hidden="true">
      <polygon points="0,0 408,0 408,160 160,160 140,142 0,142" fill="var(--navy)"/>
    </svg>
    <div class="brand">
      <span class="brand-dot"></span>
      <div class="brand-text">
        <span class="brand-name">TrailReady.com</span>
        <span class="tagline">Ready for Every Trail and Adventure</span>
      </div>
    </div>
    <div class="contact" style="left:245px;top:82px;color:var(--white);">www.trailready-gear.example<br>PO BOX 327<br>Pinecrest, IL 60999<br>orders@trailready-gear.example</div>
    <div class="person-name" style="left:34px;top:165px;color:var(--navy);font-size:18px;">Marek Dolan</div>
    <div class="person-title" style="left:34px;top:186px;color:var(--navy);font-size:13px;">Purchasing Manager</div>
    <div class="contact" style="left:245px;top:172px;color:var(--navy);">Cell: 555 014 2200<br>Office: 555 018 7341</div>
  </section>
  <section class="card back row-4 kraft">
    <div class="wordmark" style="left:108px;top:104px;width:210px;font-size:38px;color:var(--ink-brown);">TrailReady</div>
    <div class="frame" style="left:329px;top:23px;width:55px;height:52px;"><div class="symbol" role="img" aria-label="Handling symbol: fragile glass"></div></div>
    <div class="frame" style="left:329px;top:85px;width:55px;height:52px;"><div class="symbol" role="img" aria-label="Handling symbol: keep dry umbrella"></div></div>
    <div class="frame" style="left:329px;top:148px;width:55px;height:52px;"><div class="symbol" role="img" aria-label="Handling symbol: this side up arrows"></div></div>
  </section>
</body>
</html>
```